Visitenkarten-Design für Immobilienunternehmen
Zielgruppe
Wir sind ein Immobilienunternehmen mit 2 Büros - alle Zielgruppen, jung und alt, arm und reich, Käufer und Verkäufer, privat und gewerblich suchen ein neues hochwertiges Design für die Visitenkarte
Aufgabenstellung
seriös, nicht angestaubt, Firmenfarben (rot,blau, weiß, siehe Bilder)
2-seitg bedruckt (allgemein auf der einen Seite, personenvorstellung mit bild auf der anderen seite)
Ein Visitenkartendesign für 2 Personen

```html
<!DOCTYPE html>
<html lang="de">
<head>
<meta charset="utf-8">
<title>Visitenkarte – Jost Lindner</title>
<link rel="stylesheet" href="https://fonts.googleapis.com/css2?family=Montserrat:wght@400;700&family=Nunito:wght@900&display=swap">
<style>
  :root {
    --brand-blue: #1f2c7c;
    --text-blue: #2a3d8f;
    --brand-red: #e3201b;
    --mid-purple: #6a2a6e;
    --paper: #ffffff;
    --badge-grey: #d9dce6;
    --photo-a: #6f7a62;
    --photo-b: #b7b4ac;
  }
  * { margin: 0; padding: 0; box-sizing: border-box; }
  html, body { width: 1200px; height: 777px; overflow: hidden; background: var(--paper); }
  body { font-family: "Montserrat", sans-serif; }
  .card {
    position: relative;
    width: 1200px; height: 777px;
    background: linear-gradient(90deg, var(--brand-blue) 0%, var(--mid-purple) 55%, var(--brand-red) 100%);
    padding: 17px;
  }
  .card-inner { position: relative; width: 100%; height: 100%; background: var(--paper); }
  .portrait {
    position: absolute; left: 48px; top: 48px;
    width: 380px; height: 380px; border-radius: 50%;
    border: 6px solid var(--brand-blue);
    background: radial-gradient(circle at 55% 40%, var(--photo-b) 0%, #8f9aa8 45%, var(--photo-a) 100%);
  }
  .person { position: absolute; left: 521px; top: 58px; color: var(--text-blue); }
  .person-name {
    font-family: "Nunito", sans-serif;
    font-weight: 900; font-size: 50px; line-height: 1.15; color: var(--brand-blue);
  }
  .person-role { font-size: 31px; line-height: 47px; font-weight: 400; white-space: nowrap; }
  .contact { position: absolute; left: 521px; top: 307px; list-style: none; }
  .contact li { font-weight: 700; font-size: 30px; line-height: 54px; color: var(--brand-red); white-space: nowrap; }
  .referral {
    position: absolute; left: 55px; top: 588px;
    font-size: 30px; line-height: 42px; color: var(--text-blue); white-space: nowrap;
  }
  .partner-badge {
    position: absolute; left: 859px; top: 588px;
    width: 102px; height: 102px; background: var(--badge-grey);
  }
  .brand {
    position: absolute; left: 990px; top: 638px;
    display: flex; align-items: center; gap: 10px;
  }
  .brand-dot { width: 22px; height: 22px; border-radius: 50%; background: var(--brand-red); }
  .brand-name { font-weight: 700; font-size: 28px; color: var(--text-blue); }
</style>
</head>
<body>
  <div class="card">
    <div class="card-inner">
      <div class="portrait" role="img" aria-label="Porträtfoto von Jost Lindner"></div>

      <div class="person">
        <h1 class="person-name">Jost Lindner</h1>
        <p class="person-role">Geschäftsführer</p>
        <p class="person-role">Vestara/Norda Gutachter</p>
        <p class="person-role">für Immobilienbewertung</p>
      </div>

      <ul class="contact">
        <li>0171/5550123</li>
        <li>info@jost-lindner-immobilien.de</li>
        <li>jost-lindner-immobilien.de</li>
      </ul>

      <p class="referral">Kennen Sie jemanden, der ein Haus oder<br>eine Wohnung kaufen oder verkaufen möch-<br>te? Bitte rufen Sie mich an. Ich freue mich!</p>

      <div class="partner-badge" role="img" aria-label="Verbandsabzeichen"></div>

      <div class="brand">
        <span class="brand-dot"></span>
        <span class="brand-name">Norda</span>
      </div>
    </div>
  </div>
</body>
</html>
```